Business Card Design for Marketing Firm

Looking for business card design for higher end marketing firm. Clean but impressionable/trendy. We are a marketing firm that represents manufacturers in the foodservice equipment and supply industry. Our customers are end users such has hotels, restaurants, country clubs, convention centers and casinos as well as distributors of restaurants supplies and equipment, and manufacturers of foodservice equipment and supplies.
Target Market(s)
Hotels, Restaurants, Supply & Equipment Distributors, Foodservice Manufacturers
Industry/Entity Type
Foodservice/Hospitality
Contact Information for Business Card
Name, Title, Contact Number, Email, Website, Social Media, Address
Requirements
Must have
- Clean & Simple but Serious and Impressionable

```html
<!DOCTYPE html>
<html lang="en">
<head>
<meta charset="UTF-8">
<title>Summit Serve Reps – Business Card</title>
<link href="https://fonts.googleapis.com/css2?family=Montserrat:wght@400;600;700&display=swap" rel="stylesheet">
<style>
  :root {
    --navy: #2c2a80;
    --ink: #4a4a4f;
    --paper: #ffffff;
    --paper-shade: #ececee;
    --backdrop: #e3e3e6;
  }
  * { box-sizing: border-box; margin: 0; padding: 0; }
  html, body {
    width: 1200px; height: 1200px; overflow: hidden;
    background: var(--backdrop);
    font-family: "Montserrat", sans-serif;
  }
  .canvas { position: relative; width: 1200px; height: 1200px; }
  .card {
    position: absolute; left: 170px; width: 860px; height: 491px;
    background: linear-gradient(135deg, var(--paper) 0%, var(--paper) 45%, var(--paper-shade) 100%);
    box-shadow: 0 10px 30px rgba(0,0,0,0.18);
    overflow: hidden;
  }
  .card--front { top: 70px; }
  .card--back { top: 630px; }

  /* Brand lockup */
  .brand { position: absolute; display: flex; flex-direction: column; align-items: flex-start; }
  .brand__row { display: flex; align-items: center; gap: 12px; }
  .brand__dot { width: 16px; height: 16px; border-radius: 50%; background: var(--navy); }
  .brand__name {
    font-weight: 600; color: var(--navy); letter-spacing: 2px;
    text-transform: uppercase; white-space: nowrap;
  }
  .brand__rule { height: 1.5px; background: var(--navy); margin-top: 8px; width: 100%; }

  .card--front .brand { left: 50%; top: 190px; transform: translateX(-50%); }
  .card--front .brand__name { font-size: 30px; }

  .card--back .brand { right: 70px; bottom: 70px; }
  .card--back .brand__name { font-size: 22px; }
  .card--back .brand__dot { width: 12px; height: 12px; }

  /* Front rule with social pill */
  .front-rule {
    position: absolute; left: 0; right: 0; top: 420px;
    height: 2px; background: var(--navy);
  }
  .social-pill {
    position: absolute; left: 50%; top: 420px; transform: translate(-50%, -50%);
    display: flex; align-items: center; gap: 10px;
    padding: 8px 26px 8px 16px;
    border: 2px solid var(--navy); border-radius: 22px;
    background: var(--paper);
    font-size: 17px; color: var(--ink); white-space: nowrap;
  }
  .social-pill__mark { width: 16px; height: 16px; border-radius: 50%; background: var(--navy); }

  /* Back details */
  .person { position: absolute; left: 70px; top: 58px; }
  .person__name { font-size: 34px; font-weight: 700; color: var(--navy); }
  .person__title { font-size: 18px; color: var(--ink); margin-top: 2px; }

  .address {
    position: absolute; left: 70px; top: 200px;
    font-size: 18px; line-height: 1.45; color: var(--ink); font-style: normal;
  }
  .contacts { position: absolute; left: 70px; top: 275px; list-style: none; }
  .contacts li {
    display: flex; align-items: center; gap: 10px;
    font-size: 18px; line-height: 1.6; color: var(--ink);
  }
  .contacts svg { width: 15px; height: 15px; fill: var(--navy); flex: none; }
</style>
</head>
<body>
<main class="canvas">

  <section class="card card--front" aria-label="Card front">
    <div class="brand">
      <div class="brand__row">
        <span class="brand__dot"></span>
        <span class="brand__name">Summit Serve Reps</span>
      </div>
      <span class="brand__rule"></span>
    </div>
    <div class="front-rule"></div>
    <div class="social-pill">
      <span class="social-pill__mark"></span>
      <span>@summitservereps</span>
    </div>
  </section>

  <section class="card card--back" aria-label="Card back">
    <div class="person">
      <h1 class="person__name">Marcus Bell</h1>
      <p class="person__title">Founder &amp; Director</p>
    </div>
    <address class="address">
      4470 Elm Ridge Road<br>
      Fairhaven Maine 04021
    </address>
    <ul class="contacts">
      <li>
        <svg viewBox="0 0 24 24" aria-hidden="true"><path d="M6.6 10.8a15.2 15.2 0 0 0 6.6 6.6l2.2-2.2a1 1 0 0 1 1-.25 11.4 11.4 0 0 0 3.6.57 1 1 0 0 1 1 1V20a1 1 0 0 1-1 1A17 17 0 0 1 3 4a1 1 0 0 1 1-1h3.5a1 1 0 0 1 1 1c0 1.25.2 2.45.57 3.6a1 1 0 0 1-.25 1z"/></svg>
        (207)-555-0148
      </li>
      <li>
        <svg viewBox="0 0 24 24" aria-hidden="true"><path d="M2 5h20v14H2z M2 5l10 8 10-8" fill="none" stroke="#2c2a80" stroke-width="2"/><path d="M2 5h20l-10 8z"/></svg>
        bell@summitservereps.com
      </li>
      <li>
        <svg viewBox="0 0 24 24" aria-hidden="true"><circle cx="12" cy="12" r="10"/><path d="M2 12h20M12 2c3 3 3 17 0 20M12 2c-3 3-3 17 0 20" fill="none" stroke="#ffffff" stroke-width="1.5"/></svg>
        www.summitservereps.com
      </li>
    </ul>
    <div class="brand">
      <div class="brand__row">
        <span class="brand__dot"></span>
        <span class="brand__name">Summit Serve Reps</span>
      </div>
      <span class="brand__rule"></span>
    </div>
  </section>

</main>
</body>
</html>
```